Veltora Software Business Card Design

We are a new organization called Veltora. We are a software as a service provider. We deliver a project and program management solution via the internet, so everyone has the ability to work together and collaborate. Its an enterprise platform and we will focus on 50 plus employee company.

We have a website in place
www.veltora-demo.com

Use this as a start of producing the business card. The logo is there as well, but if you have a great and better solution...

Color scheme's could be inline with the website, but don't pin point on it. We can always change the website, logo, color scheme etc.

Target Market(s)

B2B, Projectmembers, projectmanagers, ICT, CTO, Marketing Managers

Industry/Entity Type

Software

Requirements
Must have
• Marten Kuyvelsma

Tel: +31 255 47 09 36
Mob: +31 6 927 15 062
marten@veltora-demo.com
Oostelingpad 84c
2184 KT Zuidervaart

Www.veltora-demo.com
social media links

```html
<!DOCTYPE html>
<html lang="en">
<head>
<meta charset="utf-8">
<title>Veltora Business Card</title>
<link rel="stylesheet" href="https://fonts.googleapis.com/css2?family=Questrial&display=swap">
<style>
  :root {
    --backdrop-light: #5a3517;
    --backdrop-dark: #2e1a0c;
    --card-base: #bccbd6;
    --card-line: rgba(255,255,255,0.18);
    --band-light: #2a8fe0;
    --band-dark: #0b5eae;
    --brand-orange: #e8852a;
    --ink-blue: #1d4f9c;
    --name-blue: #2f78cc;
  }
  * { box-sizing: border-box; margin: 0; padding: 0; }
  html, body { width: 1200px; height: 972px; overflow: hidden; }
  body {
    position: relative;
    background: linear-gradient(120deg, var(--backdrop-light) 0%, var(--backdrop-dark) 100%);
    font-family: "Questrial", "Century Gothic", sans-serif;
  }
  .card {
    position: absolute;
    border-radius: 22px;
    overflow: hidden;
    background-color: var(--card-base);
    background-image: repeating-linear-gradient(90deg, var(--card-line) 0 1px, transparent 1px 5px);
    box-shadow: 0 6px 18px rgba(0,0,0,0.45);
  }
  .card--front { left: 48px; top: 88px; width: 642px; height: 388px; }
  .card--back { left: 496px; top: 518px; width: 640px; height: 385px; }
  .band { position: absolute; inset: 0; width: 100%; height: 100%; }
  .holder-name {
    position: absolute; left: 154px; top: 20px;
    font-size: 28px; font-weight: 400; color: var(--name-blue);
  }
  .wordmark {
    position: absolute; color: var(--brand-orange); letter-spacing: 1px; line-height: 1;
  }
  .card--front .wordmark { left: 257px; top: 124px; font-size: 58px; }
  .contact {
    position: absolute; right: 30px; top: 244px;
    list-style: none; text-align: right;
    font-size: 20px; line-height: 32px; color: var(--ink-blue);
  }
  .contact svg { width: 17px; height: 17px; vertical-align: -2px; margin-right: 4px; fill: var(--ink-blue); }
  .back-band {
    position: absolute; left: 0; top: 0; width: 100%; height: 226px;
    background: linear-gradient(160deg, var(--band-light) 0%, var(--band-dark) 100%);
    border-bottom: 3px solid #0a4f96;
  }
  .card--back .wordmark {
    left: 0; right: 0; top: 112px; text-align: center; font-size: 28px;
  }
  .address {
    position: absolute; left: 0; right: 0; top: 294px;
    text-align: center; font-style: normal;
    font-size: 20px; line-height: 28px; color: var(--ink-blue);
  }
</style>
</head>
<body>
  <section class="card card--front">
    <svg class="band" viewBox="0 0 642 388" aria-hidden="true">
      <defs>
        <linearGradient id="bandFill" x1="0" y1="0" x2="1" y2="1">
          <stop offset="0" stop-color="#2a8fe0"/>
          <stop offset="1" stop-color="#0b5eae"/>
        </linearGradient>
      </defs>
      <path d="M0 0 H52 L142 82 H642 V228 H222 L0 68 Z" fill="url(#bandFill)"/>
      <path d="M52 0 L142 82 H642" fill="none" stroke="#8fc6f0" stroke-width="2"/>
    </svg>
    <h1 class="holder-name">Marten Kuyvelsma</h1>
    <div class="wordmark">Veltora</div>
    <ul class="contact">
      <li>Www.veltora-demo.com</li>
      <li>marten@veltora-demo.com</li>
      <li><svg viewBox="0 0 24 24"><path d="M6.6 10.8a15.1 15.1 0 0 0 6.6 6.6l2.2-2.2a1 1 0 0 1 1-.25 11.4 11.4 0 0 0 3.6.57 1 1 0 0 1 1 1V20a1 1 0 0 1-1 1A17 17 0 0 1 3 4a1 1 0 0 1 1-1h3.5a1 1 0 0 1 1 1c0 1.25.2 2.45.57 3.6a1 1 0 0 1-.25 1z"/></svg>+31 255 47 09 36</li>
      <li><svg viewBox="0 0 24 24"><path d="M8 1h8a2 2 0 0 1 2 2v18a2 2 0 0 1-2 2H8a2 2 0 0 1-2-2V3a2 2 0 0 1 2-2zm0 3v14h8V4zm4 15.5a1.2 1.2 0 1 0 0 2.4 1.2 1.2 0 0 0 0-2.4z"/></svg>+31 6 927 15 062</li>
    </ul>
  </section>

  <section class="card card--back">
    <div class="back-band"></div>
    <div class="wordmark">Veltora</div>
    <address class="address">Oostelingpad 84c<br>2184 KT Zuidervaart</address>
  </section>
</body>
</html>
```